BFO Web Site

Build a web site for Bellcrest Field Operations (BFO)

Target Market(s)

Petrochemical, Refining, and Manufacturing

Industry/Entity Type

Manufacturing

Coding

Coded - Design and coding required

Number of Pages Required

1 page

Font styles to use
Sans Serif

Colors

Designer to choose only greyscale colors for use in the design.

Requirements
Must have
• BFO is a member of WEL Project Services family of companies, along with Quimbrix, and Morvanta.
Would like BFO to mimic Quimbrix, and Morvanta in layout and functionality.
WIll use the same office address and phone # found Quimbrix and Morvanta.
The color scheme needs to match the logo colors.
The final product needs to be in word press.
would like to connect the QR code found on one-pager to the website.

Reference these websites: www.quimbrixweb.net and www.morvantaweb.net
Nice to have
• Would like to have a contact tab similar to the one found on Morvanta website. Use this email address. (BFO@WELmail.example.net)
The home page needs to have simple depictions of the problem statement, solution, and introduction to BFO. (use the video script to help, feel free to use your own words)

```html
<!DOCTYPE html>
<html lang="en">
<head>
<meta charset="utf-8">
<title>Bellcrest Field Operations</title>
<link rel="stylesheet" href="https://fonts.googleapis.com/css2?family=Khand:wght@500;600&family=Poppins:wght@400;500&display=swap">
<style>
:root{
  --ink:#1f1f1f;
  --text:#555;
  --muted:#666;
  --white:#fff;
  --stage:#ececec;
  --footer:#3f3f3f;
  --line:#222;
  --tile:#f0f0f0;
  --brand:#6b6b6b;
}
*{box-sizing:border-box;margin:0;padding:0}
html,body{width:1200px;height:2866px;overflow:hidden}
body{background:var(--stage);font-family:"Poppins",sans-serif;color:var(--text);position:relative}
.page{position:absolute;left:68px;top:0;width:1064px;height:2866px;background:var(--white);overflow:hidden}
h1,h2,h3{font-family:"Khand",sans-serif;font-weight:500;line-height:1.05}
.btn{display:inline-block;border:2px solid currentColor;border-radius:16px;padding:4px 20px;font-size:12px}

.site-header{height:92px;display:flex;align-items:center;padding:0 56px 0 100px}
.brand{display:flex;align-items:center;gap:8px;font-family:"Khand",sans-serif;font-weight:600;font-size:38px;color:var(--brand)}
.brand-dot{width:12px;height:12px;border-radius:50%;background:#8a8a8a}
.main-nav{margin-left:auto;display:flex;gap:34px;font-size:13px;color:#555;align-items:center}
.search{width:14px;height:14px}

.hero{position:relative;height:490px;color:var(--white);background:linear-gradient(90deg,#151515 0%,#2a2a2a 45%,#3a3a3a 70%,#262626 100%)}
.hero-photo{position:absolute;right:0;top:0;width:560px;height:490px;background:radial-gradient(ellipse at 55% 45%,#8a8a8a 0%,#4a4a4a 45%,#222 100%)}
.hero-copy{position:absolute;left:98px;top:96px}
.hero h1{font-size:46px;letter-spacing:.5px}
.hero ul{margin:14px 0 24px 14px;font-size:11px;line-height:18.5px}
.dots{position:absolute;left:508px;bottom:30px;display:flex;gap:8px}
.dots span{width:7px;height:7px;border-radius:50%;background:#fff}
.dots span:first-child{box-shadow:0 0 0 2px #333,0 0 0 3px #fff}

.problems{height:355px;text-align:center;padding-top:42px}
.section-title{font-size:36px;color:var(--ink);display:inline-block}
.rule{width:64px;height:3px;background:var(--line);margin:6px auto 0}
.problem-list{display:flex;justify-content:center;gap:40px;margin-top:36px}
.problem{width:156px;height:174px;padding:26px 18px 0;font-size:12px;line-height:17px;color:#555}
.problem.active{background:var(--tile)}
.problem svg{width:48px;height:48px;margin-bottom:12px}

.solution{position:relative;height:340px;color:var(--white);padding:78px 0 0 100px;background:linear-gradient(100deg,#101010 0%,#262626 45%,#5a5a5a 80%,#333 100%)}
.solution h2{font-size:40px}
.solution .rule,.howto .rule{margin:6px 0 0;background:#fff;width:80px}
.solution p{width:474px;font-size:13.5px;line-height:21px;margin:22px 0 24px}

.intro{position:relative;height:246px;padding:38px 0 0 102px;z-index:2}
.intro h2{font-size:38px;color:var(--ink)}
.intro p{width:520px;font-size:13px;line-height:20px;margin:18px 0 16px}
.intro .btn{color:var(--ink)}
.intro-brand{position:absolute;left:715px;top:76px;font-family:"Khand",sans-serif;font-weight:600;font-size:78px;color:var(--brand);display:flex;align-items:center;gap:12px}
.intro-brand .brand-dot{width:20px;height:20px}

.arrow{position:absolute;left:0;top:1100px;width:1064px;height:560px;z-index:1}

.howto{position:relative;height:478px;color:var(--white);background:linear-gradient(90deg,#2e2e2e 0%,#444 40%,#2c2c2c 75%,#1e1e1e 100%)}
.howto-col{position:absolute}
.howto h2{font-size:38px}
.howto p{font-size:12.5px;line-height:20px;margin-top:22px}
.col-specific{left:102px;top:70px;width:384px}
.col-general{left:575px;top:220px;width:360px}

.value{height:383px;padding:56px 102px 0}
.value h2{font-size:38px;color:var(--ink)}
.value p{font-size:12.8px;line-height:22.4px;margin-top:30px;color:var(--muted)}

.contact{height:234px;text-align:center;color:var(--white);padding-top:36px;background:linear-gradient(120deg,#222 0%,#3d3d3d 50%,#262626 100%)}
.contact h2{font-size:38px}
.contact .rule{background:#fff;width:80px}
.contact p{width:640px;margin:18px auto 18px;font-size:12.5px;line-height:20px}

.site-footer{height:248px;background:var(--footer);color:#ddd;position:relative;padding:40px 0 0 85px}
.footer-about{width:260px}
.footer-about .brand{font-size:30px;color:#ddd}
.footer-about .brand-dot{background:#ccc;width:10px;height:10px}
.footer-about p{font-size:10px;line-height:16px;margin-top:16px}
.footer-col{position:absolute;top:46px}
.footer-col h3{font-family:"Poppins",sans-serif;font-weight:500;font-size:15px;color:#fff;margin-bottom:20px}
.footer-col ul{list-style:none;font-size:10px;line-height:15px}
.col-links{left:449px}
.col-contact{left:655px;width:210px}
.col-contact li{display:flex;align-items:center;gap:12px;margin-bottom:12px;font-size:9.5px}
.col-contact svg{width:14px;height:14px;flex:none}
.col-follow{left:873px}
.socials{display:flex;gap:12px}
.socials span{width:16px;height:16px;border-radius:50%;border:1.5px solid #fff}
.copyright{position:absolute;left:84px;right:84px;bottom:0;height:36px;border-top:1px solid #666;text-align:center;font-size:9.5px;line-height:36px;color:#ccc}
</style>
</head>
<body>
<div class="page">

  <header class="site-header">
    <div class="brand"><span class="brand-dot"></span>BFO</div>
    <nav class="main-nav">
      <span>Home</span><span>Solution</span><span>Support</span><span>Resources</span><span>Communications</span><span>Contact</span>
      <svg class="search" viewBox="0 0 14 14"><circle cx="6" cy="6" r="4.5" fill="none" stroke="#333" stroke-width="2"/><line x1="9.3" y1="9.3" x2="13" y2="13" stroke="#333" stroke-width="2"/></svg>
    </nav>
  </header>

  <section class="hero">
    <div class="hero-photo" role="img" aria-label="Photo of a businessman holding a tablet with glowing data dashboards"></div>
    <div class="hero-copy">
      <h1>REMOTE PLANNING &amp;<br>SCHEDULING</h1>
      <ul>
        <li>Fixed Price. Zero Cost Escalation</li>
        <li>Reduce Cost</li>
        <li>Reduce personnel on site</li>
        <li>Productivity Gains</li>
        <li>Easy to Monitor Progress</li>
      </ul>
      <span class="btn">View Features</span>
    </div>
    <div class="dots"><span></span><span></span><span></span></div>
  </section>

  <section class="problems">
    <h2 class="section-title">THE PROBLEMS</h2>
    <div class="rule"></div>
    <div class="problem-list">
      <div class="problem">
        <svg viewBox="0 0 48 48" fill="none" stroke="#333" stroke-width="1.6"><rect x="6" y="10" width="32" height="30"/><line x1="6" y1="17" x2="38" y2="17"/><line x1="13" y1="6" x2="13" y2="13"/><line x1="31" y1="6" x2="31" y2="13"/><path d="M10 22h24M10 27h24M10 32h24M16 17v21M22 17v21M28 17v21"/><circle cx="38" cy="38" r="6" fill="#fff"/><path d="M35 38l2 2 4-4"/></svg>
        <div>High cost for turnaround planning and scheduling</div>
      </div>
      <div class="problem active">
        <svg viewBox="0 0 48 48" fill="none" stroke="#333" stroke-width="1.6"><circle cx="12" cy="10" r="3"/><circle cx="36" cy="10" r="3"/><circle cx="24" cy="30" r="3"/><path d="M7 20a5 5 0 0 1 10 0M31 20a5 5 0 0 1 10 0M19 40a5 5 0 0 1 10 0"/><path d="M16 26l4 2M32 26l-4 2" stroke-dasharray="2 2"/></svg>
        <div>Safety risks, social distancing issues</div>
      </div>
      <div class="problem">
        <svg viewBox="0 0 48 48" fill="none" stroke="#333" stroke-width="1.6"><path d="M18 10l12 4v10c0 8-6 13-12 15-6-2-12-7-12-15V14z"/><circle cx="34" cy="12" r="4"/><path d="M28 40V24a6 6 0 0 1 12 0v16z"/></svg>
        <div>Legal liabilities, co-employment issues</div>
      </div>
      <div class="problem">
        <svg viewBox="0 0 48 48" fill="none" stroke="#333" stroke-width="1.6"><path d="M10 8h28M24 8v6M18 14h12v12H18zM24 26v12M20 38h8l-4 6z"/><path d="M12 40l-4 2M36 40l4 2"/></svg>
        <div>Distraction due to plant upsets, or site interferences</div>
      </div>
    </div>
  </section>

  <section class="solution" role="img" aria-label="Photo of a refinery at sunset">
    <h2>General Solution:</h2>
    <div class="rule"></div>
    <p>A customizable solution that you pay for one time. That reduces the owner's risk, is not impacted by site conditions or limitations, is transparent, and accountable for planning and scheduling turnarounds.</p>
    <span class="btn">View Features</span>
  </section>

  <section class="intro">
    <h2>INTRODUCE PRODUCT</h2>
    <p>Bellcrest Field Operations is a new way of providing the same process of developing job plans, work packages, and turnaround schedules for a fraction of the cost of conventional methods.</p>
    <span class="btn">Get Started</span>
    <div class="intro-brand"><span class="brand-dot"></span>BFO</div>
  </section>

  <section class="howto" role="img" aria-label="Photo of engineers in hard hats at an industrial plant">
    <div class="howto-col col-specific">
      <h2>HOW IT WORKS (SPECIFIC)</h2>
      <p>How BFO works: An onsite team is to collects all the necessary information required to develop job plans. Then share it with the remote team using a planning software that both sides can access. The remote team then uses the information and documents to establish job plans and work packages. A scheduler can then develop a turnaround schedule from the completed job plans from WEL's office, where WEL's management staff can monitor, manage, and provide expert guidance to the team. By using current technology and some industry's best tools. Everyone will be able to track performance, collaborate, and share information quickly and easily. All this for a fixed price per package.</p>
    </div>
    <div class="howto-col col-general">
      <h2>HOW IT WORKS (GENERAL)</h2>
      <p>BFO still follows all the industry rules for planning and scheduling. But we now are able to perform a large portion of the processes off-site / remotely. By doing this reduces cost, minimizes client's exposer to legal liabilities, and can improve efficiencies.</p>
    </div>
  </section>

  <svg class="arrow" viewBox="0 0 1064 560" aria-hidden="true"><polygon points="857,59 1064,296 743,541 762,422 0,422 0,177 809,177" fill="#fff"/></svg>

  <section class="value">
    <h2>VALUE PROP (EXCLUSIVE BENEFITS)</h2>
    <p>Clients no longer have to struggle with the recruiting process and reviewing resumes to find the right candidates. BFO is able to attract top resources, that will consistently deliver a product that you will pay for once. No overtime or perdiem cost, just a simple fixed rate per package is all you will have to pay. We will minimize our client's exposure to legal liabilities and co-employment issues that do come up from time to time by having employees on site. Smaller events will be able to take full advantage of a well-developed planning and scheduling process that would typically be too expensive. The larger events can reduce the risk of cost overrun, reducing the size of their planning facilities. It also minimizes the opportunity for exposure to on-site injuries, widespread sicknesses, or other risks that come from having personnel on-site. No matter your situation, we have a solution customizable to fit your needs. Our staff is scalable to handle almost any situation. Let us know what you need, and we will provide you with a final product that you pay for when you are happy with it.</p>
  </section>

  <section class="contact" role="img" aria-label="Photo of hands reviewing documents on a desk">
    <h2>CONTACT NOW</h2>
    <div class="rule"></div>
    <p>Give WEL a call and ask about our Bellcrest Field Operations services and how we can provide a solution for your next turnaround that will create savings for you.</p>
    <span class="btn">Get Started</span>
  </section>

  <footer class="site-footer">
    <div class="footer-about">
      <div class="brand"><span class="brand-dot"></span>BFO</div>
      <p>A customizable solution that you pay for one time. That reduces the owner's risk, is not impacted by site conditions or limitations, is transparent, and accountable for planning and scheduling turnarounds.</p>
    </div>
    <div class="footer-col col-links">
      <h3>QUICK LINKS</h3>
      <ul><li>Home</li><li>Solution</li><li>Support</li><li>Resources</li><li>Communication</li></ul>
    </div>
    <div class="footer-col col-contact">
      <h3>CONTACT US</h3>
      <ul>
        <li><svg viewBox="0 0 14 14" fill="none" stroke="#ddd"><path d="M1 7l6-5 6 5M3 6v7h8V6"/></svg>4400 Harbor Loop South, Ste.<br>210 Ridgeport, Texas 77500</li>
        <li><svg viewBox="0 0 14 14" fill="#ddd"><path d="M3 1l3 3-2 2c1 2 2 3 4 4l2-2 3 3-2 2C6 13 1 8 1 3z"/></svg>+1 555-014-2290</li>
        <li><svg viewBox="0 0 14 14" fill="none" stroke="#ddd"><rect x="1" y="3" width="12" height="8"/><path d="M1 3l6 5 6-5"/></svg>info@quimbrixweb.net</li>
      </ul>
    </div>
    <div class="footer-col col-follow">
      <h3>FOLLOW US</h3>
      <div class="socials"><span></span><span></span><span></span><span></span></div>
    </div>
    <div class="copyright">© copyright 2021 All Right Reserved BFO</div>
  </footer>

</div>
</body>
</html>
```